6 page (for now) squarespace website design for a Mobile Fitness small business

My sons California based small business "Brindle Motion Coaching" with new subsidiary called "Brindle Motion 4 Kids". I don't understand coding the website, is that the function squarespace provides?
In the end I want a working website, squarespace, I have a google workspace domain, email and subscription to squarespace & google workspace. URLs include brindlemotioncoaching.example and brindlemotion4kids.example. I have an idea of what I am looking for in a website and I have some examples of website designs I like, but I am 100% open to your design concepts and artistic flair. email is corwin@brindlemotioncoaching.example
I am looking for someone to design the site, help me understand how to make "minor" changes and hopefully have a long term relationship on the tech side of the business. I need an Idea of pricing for future changes (Rate T&M).
There are 2 businesses so I need a way to incorporate both the main company and a subsidiary into 1 website or link it somehow. I am open to your suggestions how to accomplish that. Do I need 2 completely separate websites or can it be done on 1 site directing you to different pages. I read conflicting info if it is a BAD idea to link 2 different websites so I will defer to your advice.
Below are the pages I need designed:
- Home Page- Brindle Motion Coaching
- Home Page- Brindle Motion 4 Kids (Homeschool market)
- Member Page (subscription service?)
- Workouts- with video clips 1-6 min each
- About
- Contact
- FAQ's
Future work & page designs:
- Store with training subscriptions & a few merch items
- Booking Appointments
- Bookshelf
- email campaign
-Blog
I like the feel of this website:
https://quellpace.example/

```html
<!DOCTYPE html>
<html lang="en">
<head>
<meta charset="utf-8">
<title>Brindle Motion Coaching</title>
<link rel="stylesheet" href="https://fonts.googleapis.com/css2?family=Montserrat:wght@300;400;700&family=Roboto:wght@400;500;700&display=swap">
<style>
:root{
  --gold:#c4a070;
  --gold-dark:#b8915f;
  --cream:#efe8d8;
  --ink:#111214;
  --text:#555;
  --white:#fff;
  --footer:#0d0e10;
  --hero-a:#1b1f26;
  --hero-b:#3a2a22;
}
*{box-sizing:border-box;margin:0;padding:0}
html,body{width:1200px;height:4049px;overflow:hidden}
body{position:relative;font-family:"Roboto",sans-serif;color:var(--text);background:var(--white)}
.abs{position:absolute}
.heading{font-family:"Montserrat",sans-serif;font-weight:300;color:var(--ink);text-transform:uppercase;letter-spacing:.5px}
.heading b{font-weight:700}
.btn{position:absolute;display:flex;align-items:center;justify-content:center;background:var(--gold);color:var(--white);font:700 14px "Roboto",sans-serif;text-transform:uppercase;letter-spacing:.2px}
.btn.light{background:var(--white);color:var(--ink)}
.photo{position:absolute}

/* hero */
.hero{position:absolute;left:0;top:0;width:1200px;height:625px;background:radial-gradient(ellipse at 50% 35%,#5a4034 0%,var(--hero-b) 30%,var(--hero-a) 75%,#0e1014 100%)}
.logo{position:absolute;display:flex;flex-direction:column;align-items:center;color:var(--white)}
.logo .mark{width:40px;height:40px;border-radius:50%;background:var(--white)}
.logo .name{font:400 17px "Montserrat",sans-serif;letter-spacing:4px;margin-top:14px;white-space:nowrap}
.nav{position:absolute;left:320px;top:50px;display:flex;gap:23px;font:500 15px "Roboto",sans-serif;color:var(--white)}
.nav .active{color:var(--gold);border-bottom:2px solid var(--gold);padding-bottom:5px}
.hero-title{left:0;width:1200px;top:222px;text-align:center;font-size:44px;color:var(--white)}
.hero-copy{left:340px;width:520px;top:288px;text-align:center;font-size:17px;line-height:27px;color:var(--white)}

/* about */
.about-copy{left:111px;width:434px;font-size:14px;line-height:26.5px;text-align:justify}

/* cards */
.card-title{position:absolute;text-align:center;font:700 21px "Roboto",sans-serif;color:var(--ink)}
.card-copy{position:absolute;text-align:center;font-size:14px;line-height:26px}
.play{position:absolute;width:46px;height:46px;border-radius:50%;background:rgba(255,255,255,.55)}
.play::after{content:"";position:absolute;left:18px;top:13px;border-left:15px solid var(--white);border-top:10px solid transparent;border-bottom:10px solid transparent}

/* footer */
.footer{position:absolute;left:0;top:3781px;width:1200px;height:268px;background:var(--footer);color:var(--white)}
.footer .info{position:absolute;font-size:15px;line-height:22px}
.footer .links a{position:absolute;font-size:15px;color:var(--white);text-decoration:none}
.social{position:absolute;width:14px;height:14px;border-radius:50%;background:var(--white)}
</style>
</head>
<body>

<!-- Hero -->
<header class="hero" role="img" aria-label="Muscular athlete lifting weight plates in a dark gym with flying sparks">
</header>
<div class="logo" style="left:90px;top:18px">
  <div class="mark"></div>
  <div class="name">BRINDLE MOTION</div>
</div>
<nav class="nav">
  <span class="active">Home</span><span>Member</span><span>Workouts</span><span>About</span><span>Store</span><span>Bookshelf</span><span>Blog</span><span>Contact</span>
</nav>
<div class="btn" style="left:909px;top:39px;width:179px;height:43px;font-size:14px;text-transform:none">Booking Appointments</div>
<h1 class="abs heading hero-title" style="color:var(--white)">Brindle <b>Motion</b></h1>
<p class="abs hero-copy">Lorem ipsum dolor sit amet, consectetur adipiscing elit, eiusmod incididunt ut labore et dolore magna aliqua.</p>
<div class="btn" style="left:394px;top:366px;width:196px;height:42px">Brindle Motion Coaching</div>
<div class="btn light" style="left:609px;top:366px;width:195px;height:42px">Brindle Motion 4 Kids</div>

<!-- About -->
<h2 class="abs heading" style="left:110px;top:748px;font-size:44px">About <b>Us</b></h2>
<p class="abs about-copy" style="top:815px">Lorem ipsum dolor sit amet, consectetur adipiscing elit, sed do eiusmod tempor incididunt ut labore et dolore magna aliqua. Ut enim ad minim veniam, quis nostrud exercitation ullamco laboris nisi ut aliquip ex ea commodo consequat.</p>
<p class="abs about-copy" style="top:937px">Sed ut perspiciatis unde omnis iste natus error sit voluptatem accusantium doloremque laudantium, totam rem aperiam, eaque ipsa quae ab illo inventore veritatisea.</p>
<div class="btn" style="left:111px;top:1044px;width:149px;height:51px">Learn More</div>
<div class="photo" style="left:601px;top:727px;width:487px;height:399px;background:linear-gradient(135deg,#1d3f82,#0f1d3d 60%,#081022)" role="img" aria-label="Trainer coaching a man holding a plank in a blue-lit gym"></div>

<!-- Subscription -->
<section class="abs" style="left:0;top:1230px;width:1200px;height:1272px;background:var(--cream)"></section>
<h2 class="abs heading" style="left:0;width:1200px;top:1290px;text-align:center;font-size:44px">Subscription <b>Service</b></h2>

<div class="photo" style="left:111px;top:1382px;width:469px;height:278px;background:linear-gradient(135deg,#a07a5e,#6b5244 55%,#3c332e)" role="img" aria-label="Trainer guiding a woman through a suspension strap lunge in a brick gym"></div>
<div class="card-title" style="left:111px;width:469px;top:1692px">Personal Training</div>
<p class="card-copy" style="left:131px;width:429px;top:1729px">Lorem ipsum dolor sit amet, consectetur adipiscing elit, sed do eiusmod tempor incididunt ut labore et dolore magna aliqua. Ut veniam, quis laboris nisi commodo consequat.</p>
<div class="btn" style="left:270px;top:1825px;width:152px;height:42px">Subscribe Now</div>

<div class="photo" style="left:619px;top:1382px;width:469px;height:278px;background:linear-gradient(135deg,#e9edf1,#9fb0c4 55%,#5a6d85)" role="img" aria-label="Coach with headset writing notes beside a laptop"></div>
<div class="card-title" style="left:619px;width:469px;top:1692px">Online Training</div>
<p class="card-copy" style="left:639px;width:429px;top:1729px">Lorem ipsum dolor sit amet, consectetur adipiscing elit, sed do eiusmod tempor incididunt ut labore et dolore magna aliqua. Ut veniam, quis laboris nisi commodo consequat.</p>
<div class="btn" style="left:778px;top:1825px;width:152px;height:42px">Subscribe Now</div>

<div class="photo" style="left:111px;top:1913px;width:469px;height:278px;background:linear-gradient(135deg,#5f7d3a,#c98a2e 55%,#e9d59a)" role="img" aria-label="Magnifying glass over a nutrition label on a fresh salad bowl"></div>
<div class="card-title" style="left:111px;width:469px;top:2223px">Nutritional Guidance</div>
<p class="card-copy" style="left:131px;width:429px;top:2260px">Lorem ipsum dolor sit amet, consectetur adipiscing elit, sed do eiusmod tempor incididunt ut labore et dolore magna aliqua. Ut veniam, quis laboris nisi commodo consequat.</p>
<div class="btn" style="left:270px;top:2356px;width:152px;height:42px">Subscribe Now</div>

<div class="photo" style="left:619px;top:1913px;width:469px;height:278px;background:linear-gradient(135deg,#f2f4f6,#cdd3d9 55%,#8a8f96)" role="img" aria-label="Two women reviewing work on a tablet at a bright office desk"></div>
<div class="card-title" style="left:619px;width:469px;top:2223px">Business Coaching</div>
<p class="card-copy" style="left:639px;width:429px;top:2260px">Lorem ipsum dolor sit amet, consectetur adipiscing elit, sed do eiusmod tempor incididunt ut labore et dolore magna aliqua. Ut veniam, quis laboris nisi commodo consequat.</p>
<div class="btn" style="left:778px;top:2356px;width:152px;height:42px">Subscribe Now</div>

<!-- Booking -->
<section class="abs" style="left:0;top:2502px;width:1200px;height:341px;background:linear-gradient(90deg,var(--gold-dark),#c9a577 50%,var(--gold-dark))" role="img" aria-label="Warm-toned gym scene with people training"></section>
<h2 class="abs heading" style="left:0;width:1200px;top:2566px;text-align:center;font-size:42px;color:var(--white)">Booking <b>Appointments</b></h2>
<p class="abs" style="left:180px;width:840px;top:2636px;text-align:center;font-size:14px;line-height:26px;color:var(--white)">Lorem ipsum dolor sit amet, consectetur adipiscing elit, sed do eiusmod tempor incididunt ut labore et dolore magna aliqua. Ut enim ad minim veniam, quis nostrud exercitation ullamco laboris nisi ut aliquip ex ea commodo consequat.</p>
<div class="btn light" style="left:523px;top:2714px;width:154px;height:54px;font-size:15px">Book Now</div>

<!-- Workouts -->
<h2 class="abs heading" style="left:0;width:1200px;top:2916px;text-align:center;font-size:44px;font-weight:400">Our Workouts</h2>

<div class="photo" style="left:111px;top:3005px;width:313px;height:223px;background:linear-gradient(135deg,#3a3a3c,#7b5e55 55%,#2a2b2e)" role="img" aria-label="Two athletes squatting with medicine balls"></div>
<div class="play" style="left:244px;top:3094px"></div>
<div class="card-title" style="left:111px;width:313px;top:3252px;font-size:18px">Lorem ipsum dolor amet</div>
<p class="card-copy" style="left:121px;width:293px;top:3286px">Sed perspiciatis unde omnis iste natus error voluptatem accusantium totam</p>
<div class="btn" style="left:199px;top:3353px;width:137px;height:40px">Watch Now</div>

<div class="photo" style="left:443px;top:3005px;width:313px;height:223px;background:linear-gradient(135deg,#8b6f58,#4e4039 55%,#2d2a28)" role="img" aria-label="Trainer and client doing suspension strap exercises"></div>
<div class="play" style="left:576px;top:3094px"></div>
<div class="card-title" style="left:443px;width:313px;top:3252px;font-size:18px">Lorem ipsum dolor amet</div>
<p class="card-copy" style="left:453px;width:293px;top:3286px">Sed perspiciatis unde omnis iste natus error voluptatem accusantium totam</p>
<div class="btn" style="left:531px;top:3353px;width:137px;height:40px">Watch Now</div>

<div class="photo" style="left:776px;top:3005px;width:312px;height:223px;background:linear-gradient(135deg,#c9ccd0,#6f7278 55%,#2a2c30)" role="img" aria-label="Coach assisting a woman with a dumbbell exercise"></div>
<div class="play" style="left:909px;top:3094px"></div>
<div class="card-title" style="left:776px;width:312px;top:3252px;font-size:18px">Lorem ipsum dolor amet</div>
<p class="card-copy" style="left:786px;width:292px;top:3286px">Sed perspiciatis unde omnis iste natus error voluptatem accusantium totam</p>
<div class="btn" style="left:863px;top:3353px;width:137px;height:40px">Watch Now</div>

<!-- Newsletter -->
<section class="abs" style="left:0;top:3484px;width:1200px;height:297px;background:var(--gold)"></section>
<h2 class="abs heading" style="left:0;width:1200px;top:3546px;text-align:center;font-size:40px;color:var(--white)">Signup Our <b>Newsletter</b></h2>
<p class="abs" style="left:0;width:1200px;top:3598px;text-align:center;font-size:14px;color:var(--white)">Lorem ipsum dolor sit amet, consectetur adipiscing elit, sed do eiusmod tempor incididunt magna aliqua.</p>
<div class="abs" style="left:245px;top:3661px;width:708px;height:51px;border-radius:26px;background:var(--white);border:3px solid var(--white)">
  <span class="abs" style="left:28px;top:15px;font-size:13px;color:#555">Enter Email Address</span>
  <div class="btn" style="left:545px;top:0;width:157px;height:45px;border-radius:23px;font-size:15px">Signup</div>
</div>

<!-- Footer -->
<footer class="footer">
  <div class="logo" style="left:110px;top:66px">
    <div class="mark" style="width:62px;height:62px"></div>
    <div class="name" style="font-size:22px;margin-top:22px">BRINDLE MOTION</div>
  </div>
  <p class="info" style="left:110px;top:206px;font-size:12px">© 2022 Brindle Motion. all Rights Reserved</p>
  <p class="info" style="left:504px;top:84px">1480 Larkspur Avenue East,<br>Fairhaven, CA 94011</p>
  <p class="info" style="left:504px;top:146px">(555) 014-2280</p>
  <p class="info" style="left:504px;top:185px">Open Daily 10:00 - 10:00</p>
  <div class="links">
    <a style="left:908px;top:84px">Home</a><a style="left:1016px;top:84px">Store</a>
    <a style="left:908px;top:112px">Member</a><a style="left:1016px;top:112px">Bookshelf</a>
    <a style="left:908px;top:142px">Workouts</a><a style="left:1016px;top:142px">Blog</a>
    <a style="left:908px;top:170px">About</a><a style="left:1016px;top:170px">Contact</a>
  </div>
  <span class="social" style="left:968px;top:208px"></span>
  <span class="social" style="left:997px;top:208px"></span>
  <svg class="abs" style="left:1026px;top:208px" width="16" height="14" viewBox="0 0 16 14" aria-label="Email">
    <rect x="1" y="1" width="14" height="12" rx="1.5" fill="none" stroke="#fff" stroke-width="1.6"/>
    <path d="M1.5 2 L8 8 L14.5 2" fill="none" stroke="#fff" stroke-width="1.6"/>
  </svg>
</footer>

</body>
</html>
```